Breakfast Briefings / Lunch & Learn

I would like to have a double sided flyer size 8x10 to display the breakfast briefing on one side and Lunch & Learn on the other side.

Header on each side to say
2018 Calendar Breakfast Briefing (on the breakfast side)
2018 Calendar Lunch & Learn (on the lunch side)

I have attached a copy of the files we would like to use.

Learn

```html
<!DOCTYPE html>
<html lang="en">
<head>
<meta charset="utf-8">
<title>2018 Calendar – Breakfast Briefing / Lunch &amp; Learn</title>
<link href="https://fonts.googleapis.com/css2?family=Roboto:ital,wght@0,500;0,700;1,900&family=Lato:wght@400;700&display=swap" rel="stylesheet">
<style>
  :root {
    --page-bg: #e8e5e0;
    --paper: #ffffff;
    --header-blue: #0a7aa6;
    --teal: #079b8c;
    --lime: #88c32a;
    --orange: #f5820f;
    --pink: #d7345c;
    --sky-top: #cfe6f4;
    --sky-bottom: #ffffff;
    --ring-grey: #dfe4e8;
    --white: #ffffff;
  }
  * { box-sizing: border-box; margin: 0; padding: 0; }
  html, body { width: 1200px; height: 903px; overflow: hidden; background: var(--page-bg); }
  .canvas { position: relative; width: 1200px; height: 903px; }

  .flyer { position: absolute; width: 480px; height: 601px; background: var(--paper); }
  .flyer--breakfast { left: 87px; top: 126px; }
  .flyer--lunch { left: 631px; top: 127px; }

  .sky {
    position: absolute; left: 0; top: 0; width: 480px; height: 560px;
    background: linear-gradient(180deg, var(--sky-top) 0%, #e6f2fa 45%, var(--sky-bottom) 100%);
  }

  .flyer-header {
    position: absolute; left: 22px; top: 18px; width: 437px; height: 80px;
    background: var(--header-blue); color: var(--white);
    font-family: "Roboto", sans-serif; font-weight: 700; font-size: 26px;
    line-height: 32px; text-align: center; padding-top: 8px; letter-spacing: 0.3px;
  }
  .flyer--lunch .flyer-header { left: 21px; top: 19px; width: 438px; }

  .briefing-wheel { position: absolute; left: 0; top: 0; }
  .bubble-text { font-family: "Lato", sans-serif; font-size: 7.2px; fill: var(--white); text-anchor: middle; }
  .bubble-text .month { font-weight: 700; }

  .topic-list {
    position: absolute; left: 21px; top: 105px; width: 314px; height: 400px;
    background: var(--teal); list-style: none; padding: 10px 0 0 26px;
  }
  .topic { position: relative; height: 39px; padding-left: 42px; color: var(--white);
    font-family: "Lato", sans-serif; font-size: 11px; line-height: 13px; }
  .topic-month { font-weight: 700; display: block; }
  .topic-icon { position: absolute; left: 0; top: 2px; width: 16px; height: 13px; }

  .brand-band {
    position: absolute; left: 21px; top: 512px; width: 314px; height: 69px;
    background: var(--lime); display: flex; align-items: center; justify-content: center; gap: 8px;
  }
  .brand-dot { width: 10px; height: 10px; border-radius: 50%; background: var(--white); }
  .brand-name { font-family: "Lato", sans-serif; font-weight: 700; font-size: 22px; color: var(--white); letter-spacing: 3px; }

  .motto {
    position: absolute; left: 342px; top: 105px; width: 117px; height: 95px;
    background: var(--orange); color: var(--white);
    font-family: "Roboto", sans-serif; font-weight: 900; font-style: italic;
    font-size: 25px; line-height: 30px; text-align: center; padding-top: 3px;
  }
  .art-panel { position: absolute; left: 342px; top: 206px; width: 117px; height: 375px; background: var(--pink); }
</style>
</head>
<body>
<div class="canvas">

  <!-- Breakfast side -->
  <section class="flyer flyer--breakfast">
    <div class="sky" role="img" aria-label="Soft sky with light clouds"></div>
    <h1 class="flyer-header">2018 CALENDAR<br>BREAKFAST BRIEFING</h1>

    <svg class="briefing-wheel" width="480" height="601" viewBox="0 0 480 601">
      <!-- central photo area -->
      <circle cx="240" cy="334" r="92" fill="#b88a5e" role="img" aria-label="Photo of a tablet showing the briefing calendar on a wooden desk with coffee"/>
      <!-- cycle ring -->
      <circle cx="240" cy="334" r="112" fill="none" stroke="var(--ring-grey)" stroke-width="10"/>
      <g fill="var(--ring-grey)">
        <path d="M262 214 l10 8 -12 5z"/><path d="M352 300 l2 12 -11 -4z"/><path d="M322 420 l-4 12 -6 -10z"/>
        <path d="M200 450 l-12 -4 9 -8z"/><path d="M128 370 l-2 -12 10 5z"/><path d="M160 246 l4 -12 6 10z"/>
      </g>

      <g fill="none" stroke-dasharray="1.5 2.5" stroke-width="1" stroke="#556">
        <line x1="240" y1="222" x2="240" y2="185"/><line x1="296" y1="237" x2="315" y2="204"/>
        <line x1="337" y1="278" x2="371" y2="258"/><line x1="352" y1="334" x2="391" y2="334"/>
        <line x1="337" y1="390" x2="371" y2="410"/><line x1="296" y1="431" x2="315" y2="464"/>
        <line x1="240" y1="446" x2="240" y2="485"/><line x1="184" y1="431" x2="165" y2="464"/>
        <line x1="143" y1="390" x2="109" y2="410"/><line x1="128" y1="334" x2="89" y2="334"/>
        <line x1="143" y1="278" x2="109" y2="258"/><line x1="184" y1="237" x2="165" y2="204"/>
      </g>

      <g fill="var(--white)" stroke-width="2.5">
        <circle cx="240" cy="222" r="6" stroke="#f7b500"/><circle cx="296" cy="237" r="6" stroke="#f2e600"/>
        <circle cx="337" cy="278" r="6" stroke="#c9ea1a"/><circle cx="352" cy="334" r="6" stroke="#8ee51a"/>
        <circle cx="337" cy="390" r="6" stroke="#5bd42a"/><circle cx="296" cy="431" r="6" stroke="#36c936"/>
        <circle cx="240" cy="446" r="6" stroke="#2fd46a"/><circle cx="184" cy="431" r="6" stroke="#34cf8f"/>
        <circle cx="143" cy="390" r="6" stroke="#3cc8b4"/><circle cx="128" cy="334" r="6" stroke="#33b3c9"/>
        <circle cx="143" cy="278" r="6" stroke="#3a8fc9"/><circle cx="184" cy="237" r="6" stroke="#3a6ec7"/>
      </g>

      <g stroke-dasharray="1.5 1.8" stroke-width="1.4" fill="none">
        <circle cx="240" cy="149" r="35" stroke="#f7b500"/><circle cx="332.5" cy="173.8" r="35" stroke="#f2e600"/>
        <circle cx="400.2" cy="241.5" r="35" stroke="#c9ea1a"/><circle cx="425" cy="334" r="35" stroke="#8ee51a"/>
        <circle cx="400.2" cy="426.5" r="35" stroke="#5bd42a"/><circle cx="332.5" cy="494.2" r="35" stroke="#36c936"/>
        <circle cx="240" cy="519" r="35" stroke="#2fd46a"/><circle cx="147.5" cy="494.2" r="35" stroke="#34cf8f"/>
        <circle cx="79.8" cy="426.5" r="35" stroke="#3cc8b4"/><circle cx="55" cy="334" r="35" stroke="#33b3c9"/>
        <circle cx="79.8" cy="241.5" r="35" stroke="#3a8fc9"/><circle cx="147.5" cy="173.8" r="35" stroke="#3a6ec7"/>
      </g>
      <g>
        <circle cx="240" cy="149" r="30" fill="#f7b500"/><circle cx="332.5" cy="173.8" r="30" fill="#f2e600"/>
        <circle cx="400.2" cy="241.5" r="30" fill="#c9ea1a"/><circle cx="425" cy="334" r="30" fill="#8ee51a"/>
        <circle cx="400.2" cy="426.5" r="30" fill="#5bd42a"/><circle cx="332.5" cy="494.2" r="30" fill="#36c936"/>
        <circle cx="240" cy="519" r="30" fill="#2fd46a"/><circle cx="147.5" cy="494.2" r="30" fill="#34cf8f"/>
        <circle cx="79.8" cy="426.5" r="30" fill="#3cc8b4"/><circle cx="55" cy="334" r="30" fill="#33b3c9"/>
        <circle cx="79.8" cy="241.5" r="30" fill="#3a8fc9"/><circle cx="147.5" cy="173.8" r="30" fill="#3a6ec7"/>
      </g>

      <text class="bubble-text" x="240" y="140">Medical<tspan x="240" dy="9">Owen Marlow</tspan><tspan class="month" x="240" dy="9">2019</tspan><tspan class="month" x="240" dy="9">TBD</tspan></text>
      <text class="bubble-text" x="332.5" y="165" fill="#555">Sales<tspan x="332.5" dy="9">Tom Arden</tspan><tspan class="month" x="332.5" dy="9">2019</tspan><tspan class="month" x="332.5" dy="9">TBD</tspan></text>
      <text class="bubble-text" x="400.2" y="237">Finance<tspan x="400.2" dy="9">Ray Colton</tspan><tspan class="month" x="400.2" dy="9">March</tspan></text>
      <text class="bubble-text" x="425" y="325"><tspan class="month">R&amp;D</tspan><tspan x="425" dy="9">Nick</tspan><tspan x="425" dy="9">Varelas</tspan><tspan class="month" x="425" dy="9">April</tspan></text>
      <text class="bubble-text" x="400.2" y="417">Operations<tspan x="400.2" dy="9">Paul</tspan><tspan x="400.2" dy="9">Renner</tspan><tspan class="month" x="400.2" dy="9">May</tspan></text>
      <text class="bubble-text" x="332.5" y="489">Clinical/ Reg<tspan x="332.5" dy="9">Ben Hollis</tspan><tspan class="month" x="332.5" dy="9">June</tspan></text>
      <text class="bubble-text" x="240" y="510">Quality<tspan x="240" dy="9">Dean</tspan><tspan x="240" dy="9">Ashworth</tspan><tspan class="month" x="240" dy="9">July</tspan></text>
      <text class="bubble-text" x="147.5" y="485">People<tspan x="147.5" dy="9">Priya</tspan><tspan x="147.5" dy="9">Malhan</tspan><tspan class="month" x="147.5" dy="9">August</tspan></text>
      <text class="bubble-text" x="79.8" y="417">Marketing<tspan x="79.8" dy="9">Arjun</tspan><tspan x="79.8" dy="9">Sethi</tspan><tspan class="month" x="79.8" dy="9">September</tspan></text>
      <text class="bubble-text" x="55" y="325">Legal<tspan x="55" dy="9">Omar</tspan><tspan x="55" dy="9">Haddad</tspan><tspan class="month" x="55" dy="9">October</tspan></text>
      <text class="bubble-text" x="79.8" y="228">Market<tspan x="79.8" dy="9">Access</tspan><tspan x="79.8" dy="9">Karen</tspan><tspan x="79.8" dy="9">Lindqvist</tspan><tspan class="month" x="79.8" dy="9">November</tspan></text>
      <text class="bubble-text" x="147.5" y="170">TOS<tspan x="147.5" dy="9">Laura Bennett</tspan><tspan class="month" x="147.5" dy="9">December</tspan></text>
    </svg>
  </section>

  <!-- Lunch side -->
  <section class="flyer flyer--lunch">
    <h1 class="flyer-header">2018 CALENDAR<br>LUNCH &amp; LEARN</h1>

    <ul class="topic-list">
      <li class="topic"><svg class="topic-icon" viewBox="0 0 16 13"><path d="M0 6h3v7H0zM4 6l4-5c1-1 2 0 2 1l-1 3h5c1 0 2 1 1 2l-1 5c0 1-1 1-2 1H4z" fill="#e6f4f2"/></svg><span class="topic-month">March:</span>Mindfulness</li>
      <li class="topic"><svg class="topic-icon" viewBox="0 0 16 13"><path d="M0 6h3v7H0zM4 6l4-5c1-1 2 0 2 1l-1 3h5c1 0 2 1 1 2l-1 5c0 1-1 1-2 1H4z" fill="#e6f4f2"/></svg><span class="topic-month">April:</span>Nutrition and Lifestyle Coaching</li>
      <li class="topic"><svg class="topic-icon" viewBox="0 0 16 13"><path d="M0 6h3v7H0zM4 6l4-5c1-1 2 0 2 1l-1 3h5c1 0 2 1 1 2l-1 5c0 1-1 1-2 1H4z" fill="#e6f4f2"/></svg><span class="topic-month">May:</span>What is Neuromodulation?</li>
      <li class="topic"><svg class="topic-icon" viewBox="0 0 16 13"><path d="M0 6h3v7H0zM4 6l4-5c1-1 2 0 2 1l-1 3h5c1 0 2 1 1 2l-1 5c0 1-1 1-2 1H4z" fill="#e6f4f2"/></svg><span class="topic-month">June:</span>Achieve Your Goals</li>
      <li class="topic"><svg class="topic-icon" viewBox="0 0 16 13"><path d="M0 6h3v7H0zM4 6l4-5c1-1 2 0 2 1l-1 3h5c1 0 2 1 1 2l-1 5c0 1-1 1-2 1H4z" fill="#e6f4f2"/></svg><span class="topic-month">July:</span>Changing Your Life Positive Thinking</li>
      <li class="topic"><svg class="topic-icon" viewBox="0 0 16 13"><path d="M0 6h3v7H0zM4 6l4-5c1-1 2 0 2 1l-1 3h5c1 0 2 1 1 2l-1 5c0 1-1 1-2 1H4z" fill="#e6f4f2"/></svg><span class="topic-month">August:</span>Clean Eating How Do I Get Started</li>
      <li class="topic"><svg class="topic-icon" viewBox="0 0 16 13"><path d="M0 6h3v7H0zM4 6l4-5c1-1 2 0 2 1l-1 3h5c1 0 2 1 1 2l-1 5c0 1-1 1-2 1H4z" fill="#e6f4f2"/></svg><span class="topic-month">September:</span>Budgeting 101 Financial Wellness</li>
      <li class="topic"><svg class="topic-icon" viewBox="0 0 16 13"><path d="M0 6h3v7H0zM4 6l4-5c1-1 2 0 2 1l-1 3h5c1 0 2 1 1 2l-1 5c0 1-1 1-2 1H4z" fill="#e6f4f2"/></svg><span class="topic-month">October:</span>Busted! Nutrition Myths</li>
      <li class="topic"><svg class="topic-icon" viewBox="0 0 16 13"><path d="M0 6h3v7H0zM4 6l4-5c1-1 2 0 2 1l-1 3h5c1 0 2 1 1 2l-1 5c0 1-1 1-2 1H4z" fill="#e6f4f2"/></svg><span class="topic-month">November:</span>Time Management</li>
      <li class="topic"><svg class="topic-icon" viewBox="0 0 16 13"><path d="M0 6h3v7H0zM4 6l4-5c1-1 2 0 2 1l-1 3h5c1 0 2 1 1 2l-1 5c0 1-1 1-2 1H4z" fill="#e6f4f2"/></svg><span class="topic-month">December:</span>First Time Home Buyers</li>
    </ul>

    <div class="brand-band"><span class="brand-dot"></span><span class="brand-name">VELTORA</span></div>

    <div class="motto">LIFE.<br>LONG.<br>LEARN</div>
    <div class="art-panel" role="img" aria-label="Illustration of a pencil and a fork joined by an ampersand"></div>
  </section>

</div>
</body>
</html>
```